New Business Cards for Torvin Group

We need a new Business Card to compliment our new logo. We are a vibrant design, manufacture and install business providing recreation areas, public parks and Municipal spaces. We want business cards that are classy, modern and clean.

We have recently changed our logo, and are celebrating our 40th anniversary. We want business cards with a new modern design to reflect our status.

Target Market(s)

Customers

Contact Information for Business Card

We need all the details of our 3 offices as per the business card attached. Please disregard the old logo on the business card, the other three files show our new logo.

Requirements
Must have
• All info as per attached business card but with new logo.
Nice to have

```html
<!DOCTYPE html>
<html lang="en">
<head>
<meta charset="utf-8">
<title>Torvin Group – Business Card</title>
<link rel="stylesheet" href="https://fonts.googleapis.com/css2?family=Ubuntu:wght@400;500;700&display=swap">
<style>
  :root {
    --brand-red: #e2232a;
    --charcoal: #3c3c3f;
    --ink: #2e2e30;
    --card-white: #f8f8f7;
    --backdrop: #dcdcdc;
    --rule: #a9a9a9;
  }
  * { box-sizing: border-box; margin: 0; padding: 0; }
  html, body {
    width: 1200px; height: 1000px; overflow: hidden;
    background: var(--backdrop);
    font-family: "Ubuntu", sans-serif;
    color: var(--ink);
  }
  .business-card {
    position: absolute; left: 150px; top: 242px;
    width: 900px; height: 515px;
    background: var(--card-white);
    overflow: hidden;
    box-shadow: 0 6px 24px rgba(0,0,0,0.12);
  }
  .brand {
    position: absolute; left: 56px; top: 46px;
    display: flex; align-items: center; gap: 18px;
  }
  .brand-dot {
    width: 96px; height: 96px; border-radius: 50%;
    background: var(--brand-red);
  }
  .brand-name {
    font-weight: 700; font-size: 50px; line-height: 1;
    color: var(--charcoal); letter-spacing: 1px;
  }
  .person {
    position: absolute; right: 56px; top: 118px;
    text-align: right;
  }
  .person-name { font-size: 34px; font-weight: 500; color: var(--charcoal); }
  .person-title {
    font-size: 15px; letter-spacing: 3px; color: var(--brand-red);
    text-transform: uppercase; margin-top: 2px;
  }
  .person-contact { margin-top: 14px; font-size: 21px; text-align: left; line-height: 1.3; }
  .person-contact b { color: var(--brand-red); font-weight: 700; margin-right: 6px; }
  .person-accent {
    width: 56px; height: 6px; background: var(--brand-red);
    margin: 4px 0 0 auto;
  }
  .office {
    position: absolute; width: 240px;
    font-size: 16px; line-height: 1.45;
  }
  .office h3 {
    font-size: 16px; font-weight: 700; color: var(--brand-red);
    text-transform: uppercase; margin-bottom: 4px;
  }
  .office p { border-bottom: 1px dashed var(--rule); }
  .office p:last-child { border-bottom: none; }
  .office--head { left: 80px; top: 292px; }
  .office--dubai { left: 372px; top: 318px; }
  .office--qatar { left: 640px; top: 338px; }
  .office-icons {
    position: absolute; left: 40px; top: 300px;
    display: flex; flex-direction: column; gap: 8px;
  }
  .card-band { position: absolute; left: 0; bottom: 0; }
  .band-links {
    position: absolute; left: 340px; bottom: 18px;
    font-size: 19px; color: #fff; letter-spacing: .3px;
  }
  .band-links span { color: var(--brand-red); }
</style>
</head>
<body>
  <section class="business-card" aria-label="Torvin Group business card">
    <div class="brand">
      <div class="brand-dot"></div>
      <div class="brand-name">TORVIN GROUP</div>
    </div>

    <div class="person">
      <div class="person-name">Samir Haddad</div>
      <div class="person-title">Managing Partner</div>
      <div class="person-contact">
        <div><b>M</b>+971 (0)50 384 7160</div>
        <div><b>E</b>samir@torvingroup.com</div>
      </div>
      <div class="person-accent"></div>
    </div>

    <div class="office-icons" aria-hidden="true">
      <svg width="20" height="18" viewBox="0 0 20 18"><rect x="2" y="5" width="16" height="11" rx="2" fill="var(--brand-red)"/><rect x="9" y="1" width="2" height="6" fill="var(--brand-red)"/><rect x="11" y="1" width="5" height="3" fill="var(--brand-red)"/></svg>
      <svg width="20" height="18" viewBox="0 0 20 18"><path d="M4 2c-2 2-2 5 1 9s7 6 9 5l2-2-3-3-2 1c-2-1-4-3-5-5l1-2-3-3z" fill="var(--brand-red)"/></svg>
      <svg width="20" height="18" viewBox="0 0 20 18"><rect x="2" y="6" width="16" height="11" rx="1.5" fill="var(--brand-red)"/><rect x="5" y="1" width="10" height="6" fill="none" stroke="var(--brand-red)" stroke-width="1.6"/><rect x="5" y="10" width="10" height="2" fill="#fff"/></svg>
    </div>

    <div class="office office--head">
      <h3>Head Office</h3>
      <p>31842 Abu Dhabi, U.A.E.</p>
      <p>+971 (0)2 5530917</p>
      <p>+971 (0)2 5530918</p>
    </div>
    <div class="office office--dubai">
      <h3>Dubai Office</h3>
      <p>408216 Dubai, U.A.E</p>
      <p>+971 (0)4 3872054</p>
      <p>+971 (0)4 3872066</p>
    </div>
    <div class="office office--qatar">
      <h3>Qatar Office</h3>
      <p>17390 Doha, Qatar</p>
      <p>+974 44718302</p>
      <p>+974 44526174</p>
    </div>

    <svg class="card-band" width="900" height="110" viewBox="0 0 900 110" aria-hidden="true">
      <rect x="0" y="50" width="320" height="7" fill="var(--brand-red)"/>
      <path d="M0 62 H300 C318 62 322 36 345 36 H900 V110 H0 Z" fill="var(--charcoal)"/>
    </svg>
    <div class="band-links">sales@torvingroup.com | www.<span>torvingroup</span>.com</div>
  </section>
</body>
</html>
```